business card, letterhead, email signature, post card, ect...
RIDER HOLDS FAST / DREAM - BELIEVE - ACT
Thank you so much designers!
Please do not submitted any more drafts. I have many great looking one. enough for me to choose one. I will make the decision with few other people to pick the right one no later than this Saturday.
Again thank you so much!
K48302977
Hi Designers,
Thank you so much for all the beautiful job. There are so many great looking cards. It will take me a little more time to ask others to help me pick the right one. I will make my decision no later than Saturday.
Again thank you so very much! I wish can have all of them but that is not how it works. Someone have to win.
Thank you all!
Hi designers,
Thank you so much, you are so very talented. I have a lot to look thru and decide which one to choose and work with. This is a very difficult job for me. I will let you know very, very soon. I don't have time to put the stars because there are too many of them.
Thank you, thank you and good luck to all of you!
TR/KWH/JP Team
Hi Plumo,
you got all the attention from me now, that is good.
Let work on #18:
1- take the fax out from everything
2- put the word "DREAM BELIEVE ACT" under every RHF logo except for the business card because the back of the card already have that word.
3- The letterhead and envelop have to much black. My suggestion is maybe you change the logo to black and a few lines of black, red or grey to accomplished that.
4- can you name each item so I know what it is.
Thanks and have a nice day!
please upload Ai file of your logo

```html
<!DOCTYPE html>
<html lang="en">
<head>
<meta charset="utf-8">
<title>Rider Holds Fast — Business Card</title>
<link href="https://fonts.googleapis.com/css2?family=Open+Sans:wght@400;600;800&display=swap" rel="stylesheet">
<style>
  :root {
    --page-bg: #e9e7e4;
    --card-black: #0b0b0b;
    --ink-white: #f4f4f4;
    --ink-grey: #c9c9c9;
    --accent-red: #d3262d;
  }
  html, body {
    margin: 0;
    padding: 0;
    width: 1200px;
    height: 988px;
    overflow: hidden;
    background: var(--page-bg);
    font-family: "Open Sans", Arial, sans-serif;
  }
  .canvas {
    position: relative;
    width: 1200px;
    height: 988px;
  }
  .business-card {
    position: absolute;
    left: 220px;
    width: 760px;
    height: 434px;
    background: var(--card-black);
    color: var(--ink-white);
    box-shadow: 0 6px 20px rgba(0,0,0,0.25);
  }
  .card-logo-side { top: 40px; }
  .card-contact-side { top: 514px; }

  .brand {
    position: absolute;
    left: 0;
    right: 0;
    text-align: center;
  }
  .card-logo-side .brand { top: 128px; }
  .card-contact-side .brand { top: 58px; }
  .brand-mark {
    display: inline-flex;
    align-items: center;
    gap: 14px;
  }
  .brand-dot {
    width: 20px;
    height: 20px;
    border-radius: 50%;
    background: var(--accent-red);
  }
  .brand-name {
    font-weight: 800;
    font-size: 84px;
    line-height: 1;
    letter-spacing: 2px;
    color: var(--ink-white);
  }
  .brand-tagline {
    margin-top: 8px;
    font-weight: 800;
    font-size: 17px;
    letter-spacing: 2.5px;
    color: var(--ink-white);
  }

  .contact {
    position: absolute;
    top: 246px;
    left: 0;
    right: 0;
    display: flex;
    justify-content: center;
  }
  .person {
    width: 220px;
    text-align: right;
    padding-right: 18px;
    border-right: 2px solid var(--ink-grey);
  }
  .person-name {
    font-weight: 600;
    font-size: 17px;
    line-height: 1.3;
    color: var(--accent-red);
  }
  .person-title {
    font-size: 13px;
    line-height: 1.4;
    color: var(--ink-white);
  }
  .person-address {
    margin-top: 32px;
    font-size: 12.5px;
    line-height: 1.5;
    color: var(--ink-grey);
  }
  .channels {
    list-style: none;
    margin: 0;
    padding: 0 0 0 18px;
    width: 240px;
  }
  .channel {
    display: flex;
    align-items: center;
    gap: 10px;
    font-size: 13px;
    line-height: 23px;
    color: var(--ink-white);
    white-space: nowrap;
  }
  .channel-icon {
    width: 15px;
    height: 15px;
    flex: none;
  }
</style>
</head>
<body>
<main class="canvas">
  <section class="business-card card-logo-side">
    <div class="brand">
      <div class="brand-mark">
        <span class="brand-dot"></span>
        <span class="brand-name">RHF</span>
      </div>
      <div class="brand-tagline">RIDER HOLDS FAST</div>
    </div>
  </section>

  <section class="business-card card-contact-side">
    <div class="brand">
      <div class="brand-mark">
        <span class="brand-dot"></span>
        <span class="brand-name">RHF</span>
      </div>
      <div class="brand-tagline">RIDER HOLDS FAST</div>
    </div>

    <div class="contact">
      <div class="person">
        <div class="person-name">Marcus Lenner</div>
        <div class="person-title">Founder / CEO</div>
        <div class="person-address">4120 Harbor Ave. #305<br>Lakeview, FL 30418</div>
      </div>
      <ul class="channels">
        <li class="channel">
          <svg class="channel-icon" viewBox="0 0 20 20"><circle cx="10" cy="10" r="10" fill="#d3262d"/><path d="M7 5.5l2 2-1 1.3a6 6 0 0 0 3.2 3.2l1.3-1 2 2-1.3 1.5C9.5 14.5 5.5 10.5 5.5 6.8z" fill="#fff"/></svg>
          (555) 318-4420
        </li>
        <li class="channel">
          <svg class="channel-icon" viewBox="0 0 20 20"><circle cx="10" cy="10" r="10" fill="#d3262d"/><rect x="7" y="4.5" width="6" height="11" rx="1.2" fill="#fff"/><rect x="8" y="6" width="4" height="7" fill="#d3262d"/></svg>
          (555) 318-4421
        </li>
        <li class="channel">
          <svg class="channel-icon" viewBox="0 0 20 20"><circle cx="10" cy="10" r="10" fill="#d3262d"/><path d="M7 5.5l2 2-1 1.3a6 6 0 0 0 3.2 3.2l1.3-1 2 2-1.3 1.5C9.5 14.5 5.5 10.5 5.5 6.8z" fill="#fff"/></svg>
          (555) 318-4422
        </li>
        <li class="channel">
          <svg class="channel-icon" viewBox="0 0 20 20"><circle cx="10" cy="10" r="10" fill="#d3262d"/><rect x="5" y="6.5" width="10" height="7" fill="#fff"/><path d="M5 6.5l5 4 5-4" fill="none" stroke="#d3262d" stroke-width="1.2"/></svg>
          mlenner4120@mailbox.com
        </li>
        <li class="channel">
          <svg class="channel-icon" viewBox="0 0 20 20"><circle cx="10" cy="10" r="10" fill="#d3262d"/><circle cx="10" cy="10" r="5" fill="none" stroke="#fff" stroke-width="1.3"/><path d="M5 10h10M10 5c-2.5 3-2.5 7 0 10M10 5c2.5 3 2.5 7 0 10" fill="none" stroke="#fff" stroke-width="1"/></svg>
          www.riderholdsfast.com
        </li>
      </ul>
    </div>
  </section>
</main>
</body>
</html>
```